Maple Crest Yardworks Website Design

I need a 6 page website design for a company that Installs Synthetic Turf, Interlocking Pavers, and Patio Covers. We would like to see the design us "Landscaping Style" of a look and feel. Green, Blacks and Gray colors. Initially the website will be used the online brochure but landing pages will need to be built form this original design. Since this is brand new start up (actually offshoot form another company I was part of) we are limited on photography. We will need to use stock images until i can get installed projects photographed.This is a B2C site...targeting homeowners who are looking to expand their back yards or simply transition to maintenance free and drought tolerant yards. This is becoming very popular in California and along the Southwest United States.

Target Market(s)

Homeowners

Industry/Entity Type

Home Improvement

Coding

Coded - Design and coding required

Number of Pages Required

1 page

Font styles to use
Sans Serif

Colors
9bcb3b

Requirements
Must have
• Strong visuals and some graphic elements to illustrate the services.
• Here are some sample sites:
• https://brindlestoneworks.example
• https://www.lumagreenly.example/
• https://quorvatide.example/BackyardHavenPage
• https://otterlawnco.example
• https://www.sodvella.example/
• http://www.brookmeadtiles.example/
• https://faux-meadow-depot.example/
• https://terracehubsupply.example
• https://www.kettlebuildgroup.example

```html
<!DOCTYPE html>
<html lang="en">
<head>
<meta charset="utf-8">
<title>Maple Crest Yardworks</title>
<link href="https://fonts.googleapis.com/css2?family=Exo+2:wght@500;600;700&family=Oswald:wght@600&family=Raleway:wght@400;500;600&display=swap" rel="stylesheet">
<style>
:root{
  --green:#74b83a;
  --green-dark:#5fa02a;
  --ink:#111111;
  --text:#555555;
  --muted:#8a8a8a;
  --wood:#2b2019;
  --footer:#1a1d15;
  --white:#ffffff;
}
*{margin:0;padding:0;box-sizing:border-box}
html,body{width:1200px;height:3667px;overflow:hidden}
body{position:relative;background:var(--white);font-family:"Raleway",sans-serif;color:var(--text)}
.abs{position:absolute}
.center{left:0;width:1200px;text-align:center}
.heading{font-family:"Exo 2",sans-serif;font-weight:600;color:var(--ink);letter-spacing:-1px}

/* top bar */
.topbar{top:0;left:0;width:1200px;height:41px;background:var(--green);color:var(--white);font-size:15px;font-weight:500;display:flex;align-items:center;justify-content:center;gap:8px}
.topbar b{color:#101010;font-weight:600}

/* hero */
.hero{top:41px;left:0;width:1200px;height:657px;
  background:linear-gradient(180deg,#f4f6f2 0%,#c9d3c5 14%,#7f8f83 30%,#6c7c5c 48%,#5c8a2e 62%,#4e8a22 80%,#3f7a1c 100%);
  clip-path:polygon(0 0,100% 0,100% 564px,50% 657px,0 564px)}
.hero-shade{top:41px;left:0;width:1200px;height:150px;background:linear-gradient(180deg,rgba(255,255,255,.95),rgba(255,255,255,0))}
.nav{top:70px;left:0;width:1200px;height:40px}
.nav a{position:absolute;top:0;height:40px;line-height:40px;font-size:15px;font-weight:500;color:#111;text-decoration:none;font-family:"Raleway",sans-serif}
.nav a.active{background:var(--green);color:#fff;border-radius:20px;padding:0 19px}
.logo{top:60px;left:470px;width:260px;text-align:center;font-family:"Exo 2",sans-serif;font-weight:700;font-size:25px;line-height:28px;color:#1a1a1a;letter-spacing:1px;text-transform:uppercase}
.hero-title{top:283px;font-family:"Oswald",sans-serif;font-weight:600;font-size:60px;line-height:72px;color:#fff;text-transform:uppercase;letter-spacing:-0.5px}
.phone-btn{height:56px;width:296px;border-radius:28px;background:var(--green);color:#fff;font-family:"Exo 2",sans-serif;font-weight:500;font-size:30px;display:flex;align-items:center;padding-left:6px;gap:14px}
.phone-btn .ico{width:44px;height:44px;border-radius:50%;background:#fff;display:flex;align-items:center;justify-content:center}

/* welcome */
.chev{left:586px;width:28px;height:28px}
.welcome-sub{top:818px;font-family:"Exo 2",sans-serif;font-weight:600;font-size:20px;color:#111}
.welcome-title{top:846px;font-size:43px}
.welcome-col{top:914px;width:380px;font-size:13.5px;line-height:27px;color:#666}
.learn{top:1052px;font-size:16px;font-style:italic;font-weight:600;color:var(--green);text-decoration:underline}

/* services */
.services-title{top:1132px;font-size:43px}
.services-band{top:1378px;left:0;width:1200px;height:339px;background:var(--green)}
.card-img{top:1226px;width:323px;height:269px}
.card-title{top:1520px;width:323px;text-align:center;font-family:"Exo 2",sans-serif;font-weight:500;font-size:21px;color:#fff;text-transform:uppercase}
.card-text{top:1566px;width:323px;text-align:center;font-size:13.5px;line-height:25px;color:#fff}
.card-arrow{top:1638px;width:323px;text-align:center}

/* contact band */
.contact-band{top:1717px;left:0;width:1200px;height:417px;background:linear-gradient(180deg,#3a3a22 0%,#2e251c 35%,var(--wood) 100%)}
.contact-text{top:1858px;font-family:"Exo 2",sans-serif;font-weight:500;font-size:31px;line-height:47px;color:#fff;text-transform:uppercase}

/* gallery */
.gallery-title{top:2190px;font-size:43px}
.gallery-text{top:2259px;left:260px;width:680px;text-align:center;font-size:13.5px;line-height:27px;color:#777}
.gal-img{top:2352px;width:396px;height:291px}
.gal-overlay{background:rgba(116,184,58,.82);display:flex;align-items:center;justify-content:center}
.round-btn{top:2677px;width:46px;height:46px;border:1.5px solid var(--green);border-radius:50%;display:flex;align-items:center;justify-content:center}

/* testimonial */
.say-title{top:2778px;font-size:43px}
.avatar{top:2865px;left:543px;width:114px;height:114px;border-radius:50%;background:radial-gradient(circle at 50% 40%,#8fbf5a,#4f8a2a 70%,#3d6f20)}
.quote-badge{top:2883px;left:626px;width:38px;height:38px;border-radius:50%;background:var(--green);border:3px solid #fff;color:#fff;font-family:"Exo 2",sans-serif;font-weight:700;font-size:26px;line-height:40px;text-align:center}
.quote{top:3032px;left:255px;width:690px;text-align:center;font-size:15px;font-style:italic;line-height:29px;color:#555}
.client-name{top:3141px;font-family:"Exo 2",sans-serif;font-size:16px;font-weight:600;color:var(--green);text-transform:uppercase}
.side-arrow{top:2979px}

/* newsletter */
.newsletter{top:3229px;left:0;width:1200px;height:88px;background:var(--green)}
.news-label{top:3257px;left:100px;font-family:"Exo 2",sans-serif;font-weight:500;font-size:26px;color:#fff;text-transform:uppercase}
.news-input{top:3251px;left:469px;width:437px;height:45px;border-radius:23px;background:#fff;font-size:13px;color:#555;padding-left:18px;line-height:45px}
.news-btn{top:3251px;left:914px;width:166px;height:45px;border-radius:23px;border:1.5px solid #fff;color:#fff;font-family:"Exo 2",sans-serif;font-weight:600;font-size:19px;text-align:center;line-height:42px;text-transform:uppercase}

/* footer */
.footer{top:3317px;left:0;width:1200px;height:350px;background:linear-gradient(180deg,#1d2216,var(--footer) 60%,#141710)}
.foot-logo{top:3425px;left:84px;width:240px;font-family:"Exo 2",sans-serif;font-weight:700;font-size:27px;line-height:31px;color:#fff;letter-spacing:1px;text-transform:uppercase}
.foot-head{top:3352px;font-family:"Exo 2",sans-serif;font-weight:600;font-size:19px;color:#fff;text-transform:uppercase}
.sitemap{top:3396px;left:376px;list-style:none}
.sitemap li{height:30px;font-size:13.5px;color:#ccc;display:flex;align-items:center;gap:14px}
.sitemap li::before{content:"";width:6px;height:6px;border-radius:50%;background:var(--green)}
.news-item{left:582px;width:230px;display:flex;gap:14px}
.news-thumb{width:52px;height:52px;border-radius:50%;flex:none;background:linear-gradient(160deg,#a9b3a8,#5d7d3a)}
.news-item p{font-size:13px;line-height:19px;color:#ccc}
.news-item span{display:block;font-size:12px;color:var(--green)}
.contact-row{left:878px;width:240px;display:flex;gap:14px;font-size:13px;line-height:20px;color:#ccc}
.foot-rule{top:3604px;left:78px;width:1044px;height:1px;background:#3a3d33}
.copyright{top:3628px;left:78px;font-size:13px;color:#ddd}
.copyright em{font-style:normal;color:var(--green)}
.social{top:3629px;width:16px;height:16px;border-radius:50%}
</style>
</head>
<body>

<div class="abs topbar">FREE Design Consultation : <b>Start My Projects</b></div>

<div class="abs hero" role="img" aria-label="Photo of a grey suburban house with a trimmed green lawn and shrubs"></div>
<div class="abs hero-shade"></div>

<nav class="abs nav">
  <a class="active" style="left:164px">HOME</a>
  <a style="left:273px">ABOUT</a>
  <a style="left:367px">SERVICES</a>
  <a style="left:756px">GALLERY</a>
  <a style="left:862px">NEWS</a>
  <a style="left:940px">CONTACT</a>
  <svg style="position:absolute;left:1045px;top:13px" width="14" height="14" viewBox="0 0 14 14"><circle cx="5.5" cy="5.5" r="4.2" fill="none" stroke="#111" stroke-width="2"/><line x1="8.6" y1="8.6" x2="13" y2="13" stroke="#111" stroke-width="2.2"/></svg>
</nav>
<div class="abs logo">Maple Crest<br>Yardworks</div>

<h1 class="abs center hero-title">We are expert in outdoor<br>living landscaping</h1>
<div class="abs phone-btn" style="top:450px;left:452px">
  <span class="ico"><svg width="24" height="24" viewBox="0 0 24 24"><path d="M6.6 10.8c1.4 2.8 3.8 5.1 6.6 6.6l2.2-2.2c.3-.3.7-.4 1-.2 1.1.4 2.3.6 3.6.6.6 0 1 .4 1 1V20c0 .6-.4 1-1 1C10.6 21 3 13.4 3 4c0-.6.4-1 1-1h3.5c.6 0 1 .4 1 1 0 1.3.2 2.5.6 3.6.1.3 0 .7-.2 1z" fill="#74b83a"/></svg></span>
  (123 ) 456 7890
</div>

<svg class="abs chev" style="top:759px" viewBox="0 0 28 28"><path d="M0 2 L14 12 L28 2 L14 27 Z" fill="#74b83a"/></svg>
<div class="abs center welcome-sub">WELCOME TO</div>
<h2 class="abs center heading welcome-title">MAPLE CREST YARDWORKS</h2>
<p class="abs welcome-col" style="left:210px;text-align:right">Lorem Ipsum is simply dummy text of the printing and typesetting industry. Lorem Ipsum has been the industry's standard dummy text ever since the 1500s, when an unknown printer took a galley</p>
<p class="abs welcome-col" style="left:610px">Lorem Ipsum is simply dummy text of the printing and typesetting industry. Lorem Ipsum has been the industry's standard dummy text ever since the 1500s, when an unknown printer took a galley</p>
<div class="abs center learn">LEARN MORE</div>

<h2 class="abs center heading services-title">OUR SERVICES</h2>
<div class="abs services-band"></div>
<div class="abs card-img" style="left:84px;background:linear-gradient(160deg,#6f9a4a,#5b4632 55%,#3f2f22)" role="img" aria-label="Photo of a worker unrolling fresh turf on soil"></div>
<div class="abs card-img" style="left:438px;background:linear-gradient(160deg,#b9bcbd,#8d9193 60%,#6c7a4e)" role="img" aria-label="Photo of an interlocking paver driveway with small shrubs"></div>
<div class="abs card-img" style="left:793px;background:linear-gradient(180deg,#8c97a6,#cfd6de 35%,#4fa3c7 60%,#4e8a2e)" role="img" aria-label="Photo of a white house with a pool and patio lounge chairs"></div>

<div class="abs card-title" style="left:76px;top:1520px">NSTALLS SYNTHETIC TURF</div>
<div class="abs card-title" style="left:438px;top:1520px">INTERLOCKING PAVERS</div>
<div class="abs card-title" style="left:793px;top:1524px">PATIO COVERS</div>
<p class="abs card-text" style="left:76px">Lorem Ipsum is simply dummy text of the<br>printing &amp; type setting industry.</p>
<p class="abs card-text" style="left:438px">Lorem Ipsum is simply dummy text of the<br>printing &amp; type setting industry.</p>
<p class="abs card-text" style="left:793px">Lorem Ipsum is simply dummy text of the<br>printing &amp; type setting industry.</p>
<svg class="abs" style="left:205px;top:1639px" width="42" height="12" viewBox="0 0 42 12"><path d="M0 6H40M34 1l6 5-6 5" stroke="#fff" stroke-width="1.4" fill="none"/></svg>
<svg class="abs" style="left:580px;top:1639px" width="42" height="12" viewBox="0 0 42 12"><path d="M0 6H40M34 1l6 5-6 5" stroke="#fff" stroke-width="1.4" fill="none"/></svg>
<svg class="abs" style="left:933px;top:1639px" width="42" height="12" viewBox="0 0 42 12"><path d="M0 6H40M34 1l6 5-6 5" stroke="#fff" stroke-width="1.4" fill="none"/></svg>

<div class="abs contact-band" role="img" aria-label="Photo of a dark wooden fence with hanging ivy"></div>
<svg class="abs chev" style="top:1808px" viewBox="0 0 28 28"><path d="M0 2 L14 12 L28 2 L14 27 Z" fill="#74b83a"/></svg>
<div class="abs center contact-text">If you need an have any questio for<br>contact us on today !</div>
<div class="abs phone-btn" style="top:1973px;left:452px">
  <span class="ico"><svg width="24" height="24" viewBox="0 0 24 24"><path d="M6.6 10.8c1.4 2.8 3.8 5.1 6.6 6.6l2.2-2.2c.3-.3.7-.4 1-.2 1.1.4 2.3.6 3.6.6.6 0 1 .4 1 1V20c0 .6-.4 1-1 1C10.6 21 3 13.4 3 4c0-.6.4-1 1-1h3.5c.6 0 1 .4 1 1 0 1.3.2 2.5.6 3.6.1.3 0 .7-.2 1z" fill="#74b83a"/></svg></span>
  (123 ) 456 7890
</div>

<h2 class="abs center heading gallery-title">OUR GALLERY</h2>
<p class="abs gallery-text">Lorem Ipsum is simply dummy text of the printing and typesetting industry. Lorem Ipsum has been the industry's standard dummy text ever s printer took a galley</p>
<div class="abs gal-img" style="left:0;background:linear-gradient(180deg,#c9ccd0,#6d7a6a 45%,#2f5a22 75%,#294d1d)" role="img" aria-label="Photo of a backyard lawn with palm trees beside a covered patio"></div>
<div class="abs gal-img gal-overlay" style="left:402px;background:linear-gradient(180deg,#7fa06a,#3f7a22)" role="img" aria-label="Photo of a house behind a striped lawn, highlighted">
  <svg width="70" height="70" viewBox="0 0 70 70"><path d="M35 0V70M0 35H70" stroke="#fff" stroke-width="1.5"/></svg>
</div>
<div class="abs gal-img gal-overlay" style="left:402px;background:rgba(116,184,58,.8)">
  <svg width="70" height="70" viewBox="0 0 70 70"><path d="M35 0V70M0 35H70" stroke="#fff" stroke-width="1.5"/></svg>
</div>
<div class="abs gal-img" style="left:804px;background:linear-gradient(180deg,#4d4a52,#7a5b45 40%,#3f3a33 60%,#2f4d22)" role="img" aria-label="Photo of a covered brick patio with outdoor kitchen and putting green"></div>
<div class="abs round-btn" style="left:550px"><svg width="10" height="16" viewBox="0 0 10 16"><path d="M8 1 1 8l7 7" stroke="#74b83a" stroke-width="1.5" fill="none"/></svg></div>
<div class="abs round-btn" style="left:604px"><svg width="10" height="16" viewBox="0 0 10 16"><path d="M2 1l7 7-7 7" stroke="#74b83a" stroke-width="1.5" fill="none"/></svg></div>

<h2 class="abs center heading say-title">WHAT OUR CLIENT SAY</h2>
<div class="abs avatar" role="img" aria-label="Portrait photo of a smiling client"></div>
<div class="abs quote-badge">“</div>
<svg class="abs side-arrow" style="left:170px" width="18" height="38" viewBox="0 0 18 38"><path d="M17 1 1 19l16 18" stroke="#555" stroke-width="1.3" fill="none"/></svg>
<svg class="abs side-arrow" style="left:1004px" width="18" height="38" viewBox="0 0 18 38"><path d="M1 1l16 18L1 37" stroke="#555" stroke-width="1.3" fill="none"/></svg>
<p class="abs quote">" Lorem Ipsum is simply dummy text of the printing and typesetting industry. Lorem Ipsum has been the industry's standard dummy text ever since the when an unknown printer took a galley of type it to make specimen book. "</p>
<div class="abs center client-name">— Client Name</div>

<div class="abs newsletter"></div>
<div class="abs news-label">Sign up for newsletter</div>
<div class="abs news-input">Enter Email *</div>
<div class="abs news-btn">Subscribe</div>

<footer class="abs footer"></footer>
<div class="abs foot-logo">Maple Crest<br>Yardworks</div>

<div class="abs foot-head" style="left:379px">Sitemap</div>
<ul class="abs sitemap">
  <li>Home</li><li>About</li><li>Services</li><li>gallery</li><li>News</li><li>Contact</li>
</ul>

<div class="abs foot-head" style="left:585px">Latest News</div>
<div class="abs news-item" style="top:3397px">
  <div class="news-thumb" role="img" aria-label="Thumbnail photo of a house"></div>
  <p>Lorem Ipsum is simply<br>dummy text of<span>Today 5:60 pm - 12.06.2019</span></p>
</div>
<div class="abs news-item" style="top:3486px">
  <div class="news-thumb" role="img" aria-label="Thumbnail photo of a garden"></div>
  <p>Lorem Ipsum is simply<br>dummy text of<span>Today 2:10 pm - 15.06.2019</span></p>
</div>

<div class="abs foot-head" style="left:878px">Contact Us</div>
<div class="abs contact-row" style="top:3400px">
  <svg width="20" height="26" viewBox="0 0 20 26" style="flex:none"><path d="M10 1a8 8 0 0 0-8 8c0 6 8 15 8 15s8-9 8-15a8 8 0 0 0-8-8z" stroke="#74b83a" stroke-width="1.5" fill="none"/><circle cx="10" cy="9" r="3" stroke="#74b83a" stroke-width="1.5" fill="none"/></svg>
  <span>101 - Lorem ipsum simple text<br>of print and type text.</span>
</div>
<div class="abs contact-row" style="top:3463px">
  <svg width="20" height="20" viewBox="0 0 24 24" style="flex:none"><path d="M6.6 10.8c1.4 2.8 3.8 5.1 6.6 6.6l2.2-2.2c.3-.3.7-.4 1-.2 1.1.4 2.3.6 3.6.6.6 0 1 .4 1 1V20c0 .6-.4 1-1 1C10.6 21 3 13.4 3 4c0-.6.4-1 1-1h3.5c.6 0 1 .4 1 1 0 1.3.2 2.5.6 3.6.1.3 0 .7-.2 1z" stroke="#74b83a" stroke-width="1.5" fill="none"/></svg>
  <span>1-123-456-7890</span>
</div>
<div class="abs contact-row" style="top:3503px">
  <svg width="20" height="16" viewBox="0 0 20 16" style="flex:none"><rect x="1" y="1" width="18" height="14" stroke="#74b83a" stroke-width="1.5" fill="none"/><path d="M1 1l9 8 9-8" stroke="#74b83a" stroke-width="1.5" fill="none"/></svg>
  <span>info@maplecrestyardworks.example</span>
</div>

<div class="abs foot-rule"></div>
<div class="abs copyright">©<em>MAPLE CREST YARDWORKS</em> - 2019. All Rights Reserved</div>
<span class="abs social" style="left:958px;background:var(--green)"></span>
<span class="abs social" style="left:1007px;background:#fff"></span>
<span class="abs social" style="left:1056px;background:#fff"></span>
<span class="abs social" style="left:1107px;background:#fff"></span>

</body>
</html>
```